SLA & Internet Advert

Advertise some of our key SLA services & Internet Connectivity services.
Service Level Agreement:
Unlimited Remote, Email, Helpdesk & Telephone Support.
Unlimited Service Calls
Support Hours Monday - Saturday 7am-10pm Sunday till 5pm
Free additional visits during quorlam periods
Free remote access to school server for staff members
Free mobile device management for tablet devices
Free Email&Webhosting Service
Remote support on every device in school allowing us to close 90% of tickets within 30 mins.
Service Level Agreement Package 1 - Includes all the above + 1 Site visit every 2 weeks £2,500 per annum
Service Level Agreement Package 2 - Includes all the above + 1 Site Visit every week £4,500 per annum
Service Level Agreement Package 3 - Includes all the above + 2 Site visits every week - £7,540 per annum
Internet Connectivity (medium/large Primary)
Managed Firewall
Managed Web filter & Safeguarding
User reporting portal/email reporting.
Main Internet Line 1000 mb/s download 100mb/s upload
Back up Internet Line 80mb/s download 20mb/s upload
100% uptime guaranteed.
£3000 per annum
Internet Connectivity (Small Primary School)
Managed Firewall
£2100 per annum
My website is https://www.varnoquell.co.uk if you need any further information like phone numbers / email address etc
Education

```html
<!DOCTYPE html>
<html lang="en">
<head>
<meta charset="utf-8">
<title>SLA & Internet Advert</title>
<link href="https://fonts.googleapis.com/css2?family=Open+Sans:wght@400;600;700;800&display=swap" rel="stylesheet">
<style>
:root{
  --navy:#1d3a5c;
  --blue:#2b8fd6;
  --orange:#f08a1c;
  --text:#2a2f36;
  --grey:#eceef1;
  --grey-dark:#d5d9de;
  --white:#ffffff;
}
*{box-sizing:border-box;margin:0;padding:0}
html,body{width:849px;height:1200px;overflow:hidden;background:var(--white)}
body{font-family:'Open Sans',Arial,sans-serif;color:var(--text);position:relative}
.brand{position:absolute;left:42px;top:34px}
.brand-name{display:flex;align-items:center;gap:10px;font-size:40px;font-weight:800;color:var(--blue);letter-spacing:1px;line-height:1}
.brand-mark{width:26px;height:26px;background:var(--blue);display:inline-block}
.brand-tagline{margin-top:8px;font-size:12px;font-weight:700;color:var(--navy);letter-spacing:.5px}
.sla-title{position:absolute;left:42px;top:130px;font-size:31px;font-weight:800;color:var(--navy)}
.sla-list{position:absolute;left:46px;top:180px;list-style:none}
.sla-list li{display:flex;align-items:center;gap:14px;font-size:18px;height:27px}
.tick{width:22px;height:18px;flex:none}
.remote-note{position:absolute;left:0;width:849px;top:388px;text-align:center;font-size:18px;line-height:1.35}
.packages{position:absolute;left:42px;top:455px;width:750px;display:flex;gap:22px}
.package{flex:1;background:linear-gradient(180deg,var(--grey) 0%,var(--white) 100%);border-top:3px solid var(--grey-dark);padding:6px 12px 12px;height:232px}
.package-num{font-size:74px;font-weight:800;line-height:1;color:transparent;-webkit-text-stroke:2px var(--orange);background:linear-gradient(180deg,var(--orange),#f7b25f);-webkit-background-clip:text;background-clip:text}
.package-title{font-size:17px;font-weight:700;color:var(--navy);line-height:1.25;margin-top:4px}
.package-text{font-size:15px;line-height:1.3;margin-top:6px}
.connectivity{position:absolute;top:725px;width:360px}
.conn-left{left:42px}
.conn-right{left:430px}
.conn-head{display:flex;align-items:center;gap:14px;background:var(--grey);padding:8px 12px;border-radius:4px}
.conn-num{width:34px;height:34px;border-radius:50%;background:var(--orange);color:var(--white);font-weight:800;font-size:19px;display:flex;align-items:center;justify-content:center;flex:none}
.conn-title{font-size:13px;font-weight:700;color:var(--navy)}
.conn-list{list-style:none;margin-top:14px;padding-left:14px}
.conn-list li{position:relative;padding-left:20px;font-size:15px;line-height:1.4;margin-bottom:16px}
.conn-list li::before{content:"";position:absolute;left:0;top:8px;width:6px;height:6px;border-radius:50%;background:var(--navy)}
.footer{position:absolute;left:0;top:1130px;width:849px;height:70px;border-top:3px solid var(--blue);display:flex;align-items:center;justify-content:space-between;padding:0 42px}
.contact{display:flex;align-items:center;gap:10px;font-size:14px;color:var(--navy)}
.contact svg{width:30px;height:30px;flex:none}
.contact-address{font-size:10px;line-height:1.3;max-width:170px}
</style>
</head>
<body>
<header class="brand">
  <div class="brand-name"><span class="brand-mark"></span>VARNOQUELL</div>
  <div class="brand-tagline">EDUCATION SUPPORT &amp; INSTALLATION</div>
</header>

<h1 class="sla-title">Service Level Agreement:</h1>
<ul class="sla-list">
  <li><svg class="tick" viewBox="0 0 22 18"><path d="M2 9l6 6L20 2" fill="none" stroke="#f08a1c" stroke-width="3.5" stroke-linecap="round" stroke-linejoin="round"/></svg>Unlimited Remote, Email, Helpdesk &amp; Telephone Support.</li>
  <li><svg class="tick" viewBox="0 0 22 18"><path d="M2 9l6 6L20 2" fill="none" stroke="#f08a1c" stroke-width="3.5" stroke-linecap="round" stroke-linejoin="round"/></svg>Unlimited Service Calls</li>
  <li><svg class="tick" viewBox="0 0 22 18"><path d="M2 9l6 6L20 2" fill="none" stroke="#f08a1c" stroke-width="3.5" stroke-linecap="round" stroke-linejoin="round"/></svg>Support Hours Monday - Saturday 7am-10pm Sunday till 5pm</li>
  <li><svg class="tick" viewBox="0 0 22 18"><path d="M2 9l6 6L20 2" fill="none" stroke="#f08a1c" stroke-width="3.5" stroke-linecap="round" stroke-linejoin="round"/></svg>Free additional visits during quorlam periods</li>
  <li><svg class="tick" viewBox="0 0 22 18"><path d="M2 9l6 6L20 2" fill="none" stroke="#f08a1c" stroke-width="3.5" stroke-linecap="round" stroke-linejoin="round"/></svg>Free remote access to school server for staff members</li>
  <li><svg class="tick" viewBox="0 0 22 18"><path d="M2 9l6 6L20 2" fill="none" stroke="#f08a1c" stroke-width="3.5" stroke-linecap="round" stroke-linejoin="round"/></svg>Free mobile device management for tablet devices</li>
  <li><svg class="tick" viewBox="0 0 22 18"><path d="M2 9l6 6L20 2" fill="none" stroke="#f08a1c" stroke-width="3.5" stroke-linecap="round" stroke-linejoin="round"/></svg>Free Email&amp;Webhosting Service</li>
</ul>

<p class="remote-note">Remote support on every device in school<br>allowing us to close 90% of tickets within 30 mins.</p>

<section class="packages">
  <article class="package">
    <div class="package-num">1</div>
    <h2 class="package-title">Service Level Agreement Package 1</h2>
    <p class="package-text">Includes all the above + 1 Site visit every 2 weeks £2,500 per annum</p>
  </article>
  <article class="package">
    <div class="package-num">2</div>
    <h2 class="package-title">Service Level Agreement Package 2</h2>
    <p class="package-text">Includes all the above + 1 Site Visit every week £4,500 per annum</p>
  </article>
  <article class="package">
    <div class="package-num">3</div>
    <h2 class="package-title">Service Level Agreement Package 3</h2>
    <p class="package-text">Includes all the above + 2 Site visits every week - £7,540 per annum</p>
  </article>
</section>

<section class="connectivity conn-left">
  <div class="conn-head"><span class="conn-num">1</span><h3 class="conn-title">Internet Connectivity (medium/large Primary)</h3></div>
  <ul class="conn-list">
    <li>Managed Firewall</li>
    <li>Managed Web filter &amp; Safeguarding</li>
    <li>User reporting portal/email reporting.</li>
    <li>Main Internet Line 1000 mb/s download 100mb/s upload</li>
    <li>Back up Internet Line 80mb/s download 20mb/s upload</li>
    <li>100% uptime guaranteed.</li>
    <li>£3000 per annum</li>
  </ul>
</section>

<section class="connectivity conn-right">
  <div class="conn-head"><span class="conn-num">2</span><h3 class="conn-title">Internet Connectivity (Small Primary School)</h3></div>
  <ul class="conn-list">
    <li>Managed Firewall</li>
    <li>Managed Web filter &amp; Safeguarding</li>
    <li>User reporting portal/email reporting.</li>
    <li>Main Internet Line 1000 mb/s download 100mb/s upload</li>
    <li>£2100 per annum</li>
  </ul>
</section>

<footer class="footer">
  <div class="contact">
    <svg viewBox="0 0 30 30"><circle cx="15" cy="15" r="15" fill="#2b8fd6"/><path d="M10 8l3 0 1.5 4-2 1.5a9 9 0 0 0 4 4l1.5-2 4 1.5 0 3a2 2 0 0 1-2 2A13 13 0 0 1 8 10a2 2 0 0 1 2-2z" fill="#fff"/></svg>
    0161 555 0142
  </div>
  <div class="contact">
    <svg viewBox="0 0 30 30"><circle cx="15" cy="15" r="15" fill="#2b8fd6"/><rect x="8" y="10" width="14" height="10" rx="1" fill="#fff"/><path d="M8 10l7 6 7-6" fill="none" stroke="#2b8fd6" stroke-width="1.5"/></svg>
    info@varnoquell.co.uk
  </div>
  <div class="contact">
    <svg viewBox="0 0 30 30"><circle cx="15" cy="15" r="15" fill="#2b8fd6"/><circle cx="15" cy="15" r="7" fill="none" stroke="#fff" stroke-width="1.6"/><path d="M8 15h14M15 8c-3 4-3 10 0 14M15 8c3 4 3 10 0 14" fill="none" stroke="#fff" stroke-width="1.3"/></svg>
    varnoquell.co.uk
  </div>
  <div class="contact">
    <svg viewBox="0 0 30 30"><circle cx="15" cy="15" r="15" fill="#2b8fd6"/><path d="M15 7a5.5 5.5 0 0 1 5.5 5.5C20.5 17 15 23 15 23s-5.5-6-5.5-10.5A5.5 5.5 0 0 1 15 7z" fill="#fff"/><circle cx="15" cy="12.5" r="2" fill="#2b8fd6"/></svg>
    <span class="contact-address">Varnoquell Ltd Halden House, Mercer Street Bury Lancashire BL9 4QX</span>
  </div>
</footer>
</body>
</html>
```